Tarvel Works - Powerpoint Templates

We are a consultancy to help builders to optimize their planning in order to save building costs. For that reason we need templates for teasers and presentations where we offer our services, show our team and their capacities and present workflows, organization charts, price lists etc.

```html
<!DOCTYPE html>
<html lang="en">
<head>
<meta charset="utf-8">
<title>Tarvel Works – Presentation Templates</title>
<link href="https://fonts.googleapis.com/css2?family=Montserrat:wght@400;500;600;700;800&family=Oswald:wght@500;600&display=swap" rel="stylesheet">
<style>
:root{
  --gold:#d3a444;
  --gold-dark:#b8862c;
  --ink:#2d2d33;
  --ink-soft:#4a4a52;
  --text:#6a6a70;
  --line:#d9d9dc;
  --canvas:#8c8c8e;
  --paper:#ffffff;
  --panel:#eeeeef;
}
*{margin:0;padding:0;box-sizing:border-box}
html,body{width:1043px;height:1200px;overflow:hidden}
body{background:linear-gradient(160deg,#9a9a9c,#7d7d80);font-family:"Montserrat",sans-serif;color:var(--ink)}
.deck{position:absolute;left:29px;top:24px;display:grid;grid-template-columns:repeat(3,323px);grid-auto-rows:181px;gap:10px}
.slide{position:relative;background:var(--paper);overflow:hidden;box-shadow:0 2px 5px rgba(0,0,0,.35)}
.abs{position:absolute}
.title{position:absolute;font-size:12px;font-weight:500;letter-spacing:.2px;text-transform:uppercase;color:var(--ink);line-height:1.1}
.title b{color:var(--gold);font-weight:700}
.fine{font-size:3.9px;line-height:1.3;color:var(--text);text-align:justify}
.fine p+p{margin-top:4px}
.gold{color:var(--gold)}
.photo{position:absolute}
.footer-brand{position:absolute;left:8px;bottom:8px;display:flex;align-items:center;gap:2px;font-size:4.6px;font-weight:700;color:var(--gold);letter-spacing:.3px}
.footer-brand i{display:block;width:5px;height:5px;background:var(--ink)}
.footer-rule{position:absolute;left:0;right:0;bottom:4px;height:1px;background:var(--line)}
.footer-mark{position:absolute;right:10px;bottom:3px;width:14px;height:3px;background:var(--gold)}
.bullet{position:absolute;font-size:4px;line-height:1.3;color:var(--text);padding-left:12px}
.bullet::before{content:"";position:absolute;left:0;top:1px;border-left:4px solid var(--gold);border-top:2.5px solid transparent;border-bottom:2.5px solid transparent}
.bullet.hollow::before{border-left-color:transparent;outline:none}
.bullet.hollow::after{content:"";position:absolute;left:0;top:1px;width:3px;height:3px;border:0.6px solid var(--gold);transform:scaleX(.8)}

/* cover */
.cover .photo{inset:0;background:linear-gradient(180deg,#7b6659 0%,#5d5158 30%,#3a3b52 65%,#1d2133 100%)}
.brand{position:absolute;display:flex;align-items:center;gap:4px;font-weight:800;color:var(--gold);letter-spacing:.6px}
.brand i{display:block;background:var(--gold)}
.cover .brand{left:14px;top:52px;font-size:10px}
.cover .brand i{width:8px;height:8px}
.cover .kicker{position:absolute;left:12px;top:100px;font-size:8px;color:#fff}
.cover .big{position:absolute;left:12px;top:110px;font-size:23px;font-weight:800;color:var(--gold);line-height:1}
.cover .big2{position:absolute;left:12px;top:134px;font-size:17px;font-weight:700;color:#fff;line-height:1}
.cover .url{position:absolute;left:12px;top:165px;font-size:6px;color:#fff;letter-spacing:1.4px}

/* contents */
.contents h2{position:absolute;left:22px;top:20px;font-size:15px;font-weight:800;letter-spacing:.5px}
.contents .uline{position:absolute;left:22px;top:41px;width:48px;height:2px;background:var(--gold)}
.toc{position:absolute;width:120px}
.toc .n{position:absolute;left:0;top:0;font-size:8px;font-weight:700}
.toc .h{position:absolute;left:13px;top:0;font-size:7.5px;font-weight:600;color:var(--gold)}
.toc .fine{position:absolute;left:13px;top:10px;width:98px;text-align:left}

/* about us */
.darkpanel{position:absolute;left:0;top:32px;width:166px;height:122px;background:linear-gradient(90deg,#2f2f35,#6a6a70 85%,#b8b8bb);padding:4px 16px}
.darkpanel .fine{color:#e8e8ea}
.coin{position:absolute;width:25px;height:25px;border-radius:50%;background:radial-gradient(circle at 35% 35%,#f0c668,var(--gold-dark));box-shadow:0 0 0 2px #fff,0 0 0 3px var(--line)}
.coin svg{position:absolute;inset:6px}
.feat{position:absolute;left:203px;width:110px}
.feat h4{font-size:7px;font-weight:600;margin-bottom:2px}
.feat .fine{text-align:left}

/* education */
.eduframe{position:absolute;left:0;top:0}
.edu-label{position:absolute;width:55px;text-align:center;font-size:4.8px;font-weight:700;color:var(--gold)}
.edu-text{position:absolute;width:44px;font-size:3.2px;line-height:1.25;color:var(--text);text-align:center}

/* domain */
.ticks{position:absolute;left:20px;top:48px;list-style:none}
.ticks li{font-size:8px;color:var(--ink-soft);line-height:14.6px;padding-left:7px;position:relative}
.ticks li::before{content:"";position:absolute;left:0;top:6px;width:2.5px;height:2.5px;background:var(--gold)}

/* overview */
.legend{position:absolute;width:70px}
.legend h5{font-size:5px;font-weight:500;padding-left:7px;position:relative}
.legend h5::before{content:"";position:absolute;left:0;top:1px;width:4px;height:4px;border-radius:50%;background:var(--c)}
.legend .fine{padding-left:9px;font-size:3px;text-align:left}

/* about our project */
.dark .photo{inset:0;background:linear-gradient(160deg,#3e3e42,#2a2a2d 55%,#1e1e20)}
.projframe{position:absolute;left:100px;top:39px;width:116px;height:102px;border:1px solid #d8d8d8;text-align:center;font-family:"Oswald",sans-serif;font-weight:600;font-size:24px;line-height:1.12;color:#fff;padding-top:4px}
.projframe span{color:var(--gold)}

/* phones */
.phone{position:absolute;width:37px;border:1.6px solid var(--ink);border-radius:4px;background:#fff;padding:14px 3px 3px}
.phone::before{content:"";position:absolute;top:1px;left:12px;width:10px;height:2px;border-radius:1px;background:var(--ink)}
.phone h6{font-size:4.6px;font-weight:500;line-height:1.15;position:absolute;top:4px;left:3px;right:3px}
.phone .ico{width:6px;height:5px;border:0.6px solid var(--gold);margin:10px auto 4px}
.phone .fine{font-size:2.4px;text-align:left}

/* project thumbs */
.thumb{position:absolute;top:83px;width:69px}
.thumb .photo{position:relative;height:47px;border:1px solid var(--line)}
.thumb h5{font-size:6px;font-weight:500;color:var(--gold);margin-top:2px}
.thumb .fine{font-size:2.8px;text-align:left}

/* pricing */
.plan{position:absolute;top:31px;width:64px;height:124px;border-radius:6px;padding-top:20px}
.plan .tab{position:absolute;top:6px;left:3px;right:3px;height:12px;border-radius:6px 6px 2px 2px;font-size:5.2px;font-weight:600;color:#fff;text-align:center;line-height:12px;background:var(--ink)}
.plan .stars{position:absolute;top:0;left:0;right:0;text-align:center;font-size:5px;line-height:6px;color:var(--gold)}
.plan ul{list-style:none;padding:4px 6px 0}
.plan li{font-size:3.3px;color:#fff;line-height:8.6px;padding-left:6px;position:relative}
.plan li::before{content:"";position:absolute;left:0;top:3px;width:3px;height:3px;border-radius:50%;background:#fff}
.plan .head{font-size:2.6px;color:#eee;text-align:center;padding:0 3px}
.plan .buy{margin:4px 10px 0;border:0.6px solid #fff;border-radius:4px;background:rgba(255,255,255,.85);font-size:4px;font-weight:600;letter-spacing:.8px;text-align:center;line-height:7px;color:var(--ink)}
.plan .price{position:absolute;left:3px;bottom:-6px;width:22px;height:22px;border-radius:50%;background:#fff;border:2px solid var(--ink);font-size:7px;font-weight:500;text-align:center;line-height:18px}
.plan .price sup{font-size:3px}
.plan .note{position:absolute;left:28px;bottom:3px;width:30px;font-size:2.4px;color:#eee;text-align:center}

/* kites */
.kite-val{position:absolute;font-size:3.6px;font-weight:700;color:var(--ink)}
.kite-year{position:absolute;top:114px;width:30px;text-align:center;font-size:3.6px;font-weight:700}
.kite-text{position:absolute;top:136px;width:44px;font-size:3.2px;line-height:1.25;color:var(--text);text-align:left}

/* timeline */
.tl-label{position:absolute;width:45px}
.tl-label h6{font-size:4.8px;font-weight:500;color:var(--gold)}
.tl-label .fine{font-size:2.4px;text-align:left}
.yearbadge{position:absolute;top:131px;display:flex;align-items:center;gap:4px}
.yearbadge .dot{width:18px;height:18px;border-radius:50%;background:var(--ink);border:1.5px solid #fff;box-shadow:0 0 0 1px var(--ink);color:#fff;font-weight:800;font-size:10px;text-align:center;line-height:15px}
.yearbadge h6{font-size:8px;font-weight:500;color:var(--gold);line-height:1}
.yearbadge .fine{font-size:2.4px;text-align:left;width:34px}

/* org chart */
.band{position:absolute;left:0;right:0;top:75px;height:75px;background:var(--gold)}
.person{position:absolute;top:79px;width:64px;text-align:center}
.avatar{width:24px;height:24px;border-radius:50%;margin:0 auto;border:2px solid #fff;background:linear-gradient(160deg,#8a8a8c,#4b4b50)}
.person h5{font-size:5.6px;font-weight:700;color:var(--ink);margin-top:5px}
.person .fine{color:#fff;font-size:2.6px;text-align:center;margin-top:2px}

/* contact */
.contact .photo{right:0;top:0;width:190px;height:181px;background:linear-gradient(90deg,#ffffff 0%,#ececee 40%,#c8c8cb 75%,#dcdcde 100%)}
.contact .brand{left:12px;top:44px;font-size:12px}
.contact .brand i{width:10px;height:10px}
.contact h3{position:absolute;left:11px;top:104px;font-size:11px;font-weight:500}
.contact h3 b{color:var(--gold)}
.clist{position:absolute;left:11px;top:119px;list-style:none}
.clist li{font-size:6.4px;color:var(--ink-soft);line-height:10px;display:flex;align-items:center;gap:3px}
.clist li i{display:inline-block;width:4.5px;height:4.5px;border-radius:50%;background:var(--gold)}
.contact .url{position:absolute;left:11px;top:158px;font-size:7px;letter-spacing:1.3px;color:var(--ink-soft)}
.social{position:absolute;top:12px;right:14px;display:flex;gap:3px}
.social i{display:block;width:8px;height:8px;border-radius:1.5px;background:var(--gold)}
</style>
</head>
<body>
<main class="deck">

  <!-- 1 Cover -->
  <section class="slide cover">
    <div class="photo" role="img" aria-label="City skyline with twin towers at sunset"></div>
    <div class="brand"><i></i>TARVEL WORKS</div>
    <div class="kicker">PRESENTATION</div>
    <div class="big">BUSINESS</div>
    <div class="big2">MARKETING</div>
    <div class="url">www.tarvelworks.com</div>
  </section>

  <!-- 2 Contents -->
  <section class="slide contents">
    <h2>CONTENTS</h2><div class="uline"></div>
    <div class="toc" style="left:35px;top:58px"><span class="n">1.</span><span class="h">Lorem ipsum</span><p class="fine">Lorem ipsum dolor sit amet, consectetuer adipiscing elit, sed diam nonummy nibh</p></div>
    <div class="toc" style="left:170px;top:59px"><span class="n">2.</span><span class="h">Lorem ipsum</span><p class="fine">Lorem ipsum dolor sit amet, consectetuer adipiscing elit, sed diam nonummy nibh euismod tincid</p></div>
    <div class="toc" style="left:35px;top:96px"><span class="n">3.</span><span class="h">Lorem ipsum</span><p class="fine">Lorem ipsum dolor sit amet, consectetuer adipiscing elit, sed diam nonummy nibh</p></div>
    <div class="toc" style="left:170px;top:97px"><span class="n">4.</span><span class="h">Lorem ipsum</span><p class="fine">Lorem ipsum dolor sit amet, consectetuer adipiscing elit, sed diam nonummy nibh euismod tincid</p></div>
    <div class="toc" style="left:35px;top:134px"><span class="n">5.</span><span class="h">Lorem ipsum</span><p class="fine">Lorem ipsum dolor sit amet, consectetuer adipiscing elit, sed diam nonummy nibh</p></div>
    <div class="toc" style="left:170px;top:135px"><span class="n">6.</span><span class="h">Lorem ipsum</span><p class="fine">Lorem ipsum dolor sit amet, consectetuer adipiscing elit, sed diam nonummy nibh euismod tincid</p></div>
    <div class="footer-rule"></div><div class="footer-brand"><i></i>TARVEL WORKS</div><div class="footer-mark"></div>
  </section>

  <!-- 3 About us -->
  <section class="slide">
    <h2 class="title" style="left:16px;top:14px">About us <b>company</b></h2>
    <div class="darkpanel"><div class="fine">
      <p>Lorem ipsum dolor sit amet, consectetuer adipiscing elit, sed diam nonummy nibh euismod tincidunt ut laoreet dolore magna aliquam erat volutpat. Ut wisi enim ad minim veniam, quis nostrud exerci tation ullamcorper suscipit lobortis nisl ut aliquip ex ea commodo consequat. Duis autem vel eum iriure dolor in hendrerit in vulputate velit esse molestie consequat, vel illum dolore eu feugiat nulla facilisis at vero eros et accumsan et iusto odio dignissim qui blandit praesent luptatum zzril delenit augue duis dolore te feugait nulla facilisi.</p>
      <p>Lorem ipsum dolor sit amet, consectetuer adipiscing elit, sed diam nonummy nibh euismod tincidunt ut laoreet dolore magna aliquam erat volutpat. Ut wisi enim ad minim veniam, quis nostrud exerci tation ullamcorper suscipit lobortis nisl ut aliquip ex ea commodo consequat. Lorem ipsum dolor sit amet, consectetuer nonummy nibh euismod tincidunt ut laoreet dolore magna aliquam erat volutpat. Ut wisi enim ad minim veniam, quis nostrud exerci tation ullamcorper suscipit lobortis nisl ut aliquip ex ea commodo consequat.</p>
    </div></div>
    <div class="coin" style="left:170px;top:51px"><svg viewBox="0 0 10 10"><rect x="1" y="2" width="8" height="5" fill="none" stroke="#2d2d33" stroke-width=".9"/><path d="M3 8.5h4" stroke="#2d2d33" stroke-width=".9"/></svg></div>
    <div class="feat" style="top:53px"><h4>Lorem ipsum</h4><p class="fine">ipsum dolor sit amet, cons ectetuer adipiscing elit, sed diam nonummy nibh euismod tincidunt ut laoreet</p></div>
    <div class="coin" style="left:170px;top:90px"><svg viewBox="0 0 10 10"><path d="M2 6a2 2 0 0 1 1-4 3 3 0 0 1 5 1 1.6 1.6 0 0 1 0 3z" fill="#2d2d33"/><path d="M5 6v3M3 9h4" stroke="#2d2d33" stroke-width=".8"/></svg></div>
    <div class="feat" style="top:91px"><h4>Lorem ipsum</h4><p class="fine">ipsum dolor sit amet, cons ectetuer adipiscing elit, sed diam nonummy nibh euismod tincidunt ut laoreet dolore magna aliquam erat volutpat.</p></div>
    <div class="coin" style="left:170px;top:132px"><svg viewBox="0 0 10 10"><path d="M1 8l3-3 2 2 3-4" fill="none" stroke="#2d2d33" stroke-width=".9"/><circle cx="4" cy="5" r=".9" fill="#2d2d33"/><circle cx="6" cy="7" r=".9" fill="#2d2d33"/><circle cx="9" cy="3" r=".9" fill="#2d2d33"/></svg></div>
    <div class="feat" style="top:134px"><h4>Lorem ipsum</h4><p class="fine">ipsum dolor sit amet, cons ectetuer adipiscing elit, sed diam nonummy nibh euismod tincidunt</p></div>
    <div class="footer-rule"></div><div class="footer-brand"><i></i>TARVEL WORKS</div><div class="footer-mark"></div>
  </section>

  <!-- 4 Active intelligence -->
  <section class="slide">
    <h2 class="title" style="left:14px;top:16px">Active <b>intelligence</b></h2>
    <div class="fine abs" style="left:14px;top:33px;width:130px">
      <p>Lorem ipsum dolor sit amet, consectetuer adipiscing elit, sed diam nonummy nibh euismod tincidunt ut laoreet dolore magna aliquam erat volutpat. Ut wisi enim ad minim veniam, quis nostrud exerci tation ullamcorper suscipit lobortis nisl ut aliquip ex ea commodo consequat. Duis autem vel eum iriure dolor in hendrerit in vulputate velit esse</p>
      <p>Lorem ipsum dolor sit amet, consectetuer adipiscing elit, sed diam nonummy nibh euismod tincidunt ut laoreet dolore magna aliquam erat volutpat. Ut wisi enim ad minim veniam, quis nostrud exerci tation ullamcorper suscipit lobortis nisl ut aliquip ex ea commodo consequat. Duis autem vel eum iriure dolor in hendrerit in vulputate velit esse diam nonummy nibh euismod tincidunt ut laoreet dolore magna aliquam erat volutpat. Ut wisi enim ad minim veniam, quis nostrud exerci tation</p>
    </div>
    <div class="bullet" style="left:14px;top:120px;width:130px">Lorem ipsum dolor sit amet, consectetuer adipiscing elit, sed diam nonummy nibh euismod tincidunt ut laoreet dolore magna</div>
    <div class="bullet hollow" style="left:14px;top:142px;width:130px">Lorem ipsum dolor sit amet, consectetuer adipiscing elit, sed diam nonummy nibh euismod tincidunt ut laoreet dolore magna</div>
    <div class="abs" style="left:225px;top:24px;width:75px;height:2px;background:var(--gold)"></div>
    <div class="abs" style="left:155px;top:110px;width:2px;height:43px;background:var(--gold)"></div>
    <div class="abs" style="left:155px;top:151px;width:95px;height:2px;background:var(--gold)"></div>
    <div class="photo" style="left:160px;top:29px;width:163px;height:120px;background:linear-gradient(150deg,#d9d1c8,#8f8a86 40%,#4a4e5e 75%,#c79a5a)" role="img" aria-label="Glass skyscrapers seen from below against a cloudy sky"></div>
    <div class="footer-rule"></div><div class="footer-brand"><i></i>TARVEL WORKS</div><div class="footer-mark"></div>
  </section>

  <!-- 5 Education -->
  <section class="slide">
    <h2 class="title" style="left:10px;top:10px">Our company <b>education</b></h2>
    <svg class="eduframe" width="323" height="181" viewBox="0 0 323 181">
      <g fill="none" stroke="#2d2d33" stroke-width="1.8">
        <rect x="59" y="42" width="55" height="81" rx="6"/>
        <rect x="134" y="42" width="55" height="81" rx="6"/>
        <rect x="209" y="42" width="55" height="81" rx="6"/>
      </g>
      <g stroke="#8c8c8e" stroke-width="1.6">
        <path d="M114 106l20-38"/><path d="M189 106l20-38"/>
      </g>
      <circle cx="113" cy="62" r="2" fill="#2d2d33"/><circle cx="188" cy="62" r="2" fill="#2d2d33"/><circle cx="134" cy="105" r="2" fill="#2d2d33"/><circle cx="209" cy="105" r="2" fill="#2d2d33"/>
      <g fill="none" stroke="#d3a444" stroke-width=".8">
        <circle cx="86.5" cy="55" r="3"/><path d="M85.5 58.5h2"/>
        <rect x="157" y="52" width="8" height="6"/><path d="M157 52l4 3 4-3"/>
        <path d="M233 51v7h8M234 57l6-5"/>
      </g>
    </svg>
    <div class="edu-label" style="left:59px;top:64px">IDEA</div>
    <div class="edu-label" style="left:134px;top:64px">PROMOTION</div>
    <div class="edu-label" style="left:209px;top:63px">GROWTH</div>
    <p class="edu-text" style="left:64.5px;top:75px">Lorem ipsum dolor sit amet, consectetuer adipiscing elit, sed diam nonummy nibh euismod tincidunt ut laoreet dolore magna aliquam erat volutpat. Ut wisi enim ad minim veniam, quis nostrud</p>
    <p class="edu-text" style="left:139.5px;top:75px">Lorem ipsum dolor sit amet, consectetuer adipiscing elit, sed diam nonummy nibh euismod tincidunt ut laoreet dolore magna aliquam erat volutpat. Ut wisi enim ad minim veniam, quis nostrud</p>
    <p class="edu-text" style="left:214.5px;top:75px">Lorem ipsum dolor sit amet, consectetuer adipiscing elit, sed diam nonummy nibh euismod tincidunt ut laoreet dolore magna aliquam erat volutpat. Ut wisi enim ad minim veniam, quis nostrud</p>
    <p class="fine abs" style="left:38px;top:136px;width:248px;text-align:center">Lorem ipsum dolor sit amet, consectetuer adipiscing elit, sed diam nonummy nibh euismod tincidunt ut laoreet dolore magna aliquam erat volutpat. Ut wisi enim ad minim veniam, quis nostrud exerci tation ullamcorper suscipit lobortis nisl ut aliquip ex ea commodo consequat. Duis autem vel eum iriure dolor in hendrerit</p>
    <div class="footer-rule"></div><div class="footer-brand"><i></i>TARVEL WORKS</div><div class="footer-mark"></div>
  </section>

  <!-- 6 Domain -->
  <section class="slide">
    <h2 class="title" style="left:20px;top:11px;font-size:10px">What's a domain? It's that name up<br><b>in the address bar.</b></h2>
    <ul class="ticks">
      <li>Fits your business or products</li>
      <li>Is easy to spell and remember</li>
      <li>Fits your business or products</li>
      <li>Is easy to spell and remember</li>
      <li>Fits your business or products</li>
      <li>Is easy to spell and remember</li>
      <li>Fits your business or products</li>
    </ul>
    <div class="photo" style="left:162px;top:36px;width:135px;height:117px;background:linear-gradient(170deg,#dfe7ef,#9fb0c2 45%,#59687c)" role="img" aria-label="Office towers reaching into a pale sky"></div>
    <div class="footer-rule"></div><div class="footer-brand"><i></i>TARVEL WORKS</div><div class="footer-mark"></div>
  </section>

  <!-- 7 Company overview -->
  <section class="slide">
    <h2 class="title" style="left:10px;top:12px;font-size:12.5px">Company <b>overview</b></h2>
    <div class="fine abs" style="left:10px;top:33px;width:138px;font-size:3.7px">
      <p>Lorem ipsum dolor sit amet, consectetuer adipiscing elit, sed diam nonummy nibh euismod tincidunt ut laoreet dolore magna aliquam erat volutpat. Ut wisi enim ad minim veniam, quis nostrud exerci tation ullamcorper suscipit lobortis nisl ut aliquip ex ea commodo consequat. Duis autem vel eum iriure dolor in hendrerit</p>
      <p>Lorem ipsum dolor sit amet, consectetuer adipiscing elit, sed diam nonummy nibh</p>
      <p>m ipsum dolor sit amet, consectetuer adipiscing elit, sed diam</p>
    </div>
    <svg class="abs" style="left:160px;top:20px" width="160" height="78" viewBox="0 0 160 78" font-family="Montserrat,sans-serif" font-size="4" fill="#2d2d33">
      <g stroke="#e0e0e2" stroke-width=".4">
        <path d="M10 2h140M10 12.5h140M10 23h140M10 33.5h140M10 44h140M10 54.5h140M10 65h140"/>
      </g>
      <g text-anchor="end"><text x="7" y="4">60</text><text x="7" y="14.5">50</text><text x="7" y="25">40</text><text x="7" y="35.5">30</text><text x="7" y="46">20</text><text x="7" y="56.5">10</text><text x="7" y="67">0</text></g>
      <rect x="21" y="23" width="4" height="42" fill="#d3a444"/><rect x="27" y="12.5" width="4" height="52.5"/>
      <rect x="51" y="53.5" width="4" height="11.5"/><rect x="57" y="28" width="4" height="37" fill="#d3a444"/>
      <rect x="81" y="4" width="4" height="61"/><rect x="87" y="51" width="4" height="14" fill="#d3a444"/>
      <rect x="111" y="10.5" width="4" height="54.5" fill="#d3a444"/><rect x="117" y="34.5" width="4" height="30.5"/>
      <g text-anchor="middle"><text x="26" y="74">JAN</text><text x="56" y="74">FEB</text><text x="86" y="74">MAR</text><text x="116" y="74">APR</text></g>
    </svg>
    <svg class="abs" style="left:10px;top:96px" width="140" height="62" viewBox="0 0 140 62" font-family="Montserrat,sans-serif" font-size="3" fill="#2d2d33">
      <g stroke="#e0e0e2" stroke-width=".4"><path d="M10 2h125M10 10.3h125M10 18.6h125M10 27h125M10 35.3h125M10 43.6h125M10 52h125"/></g>
      <g text-anchor="end"><text x="7" y="3">60</text><text x="7" y="11.3">50</text><text x="7" y="19.6">40</text><text x="7" y="28">30</text><text x="7" y="36.3">20</text><text x="7" y="44.6">10</text><text x="7" y="53">0</text></g>
      <polyline fill="none" stroke="#d3a444" stroke-width=".8" points="14,43 28,48 42,30 56,12 70,22 84,35 98,27 112,18 126,44"/>
      <polyline fill="none" stroke="#2d2d33" stroke-width=".8" points="14,52 28,45 42,25 56,38 70,20 84,29 98,35 112,27 126,18"/>
      <g text-anchor="middle" font-size="2.2"><text x="14" y="58">TEXT 01</text><text x="28" y="58">TEXT 02</text><text x="42" y="58">TEXT 03</text><text x="56" y="58">TEXT 04</text><text x="70" y="58">TEXT 05</text><text x="84" y="58">TEXT 06</text><text x="98" y="58">TEXT 07</text><text x="112" y="58">TEXT 08</text><text x="126" y="58">TEXT 09</text></g>
    </svg>
    <div class="legend" style="left:170px;top:110px;--c:var(--gold)"><h5 class="gold">Lorem ipsum</h5><p class="fine">Lorem ipsum dolor sit amet, consectetuer adipiscing elit, sed diam nonummy nibh euismod</p></div>
    <div class="legend" style="left:250px;top:110px;--c:var(--ink)"><h5>Lorem ipsum</h5><p class="fine">Lorem ipsum dolor sit amet, consectetuer adipiscing elit, sed diam nonummy nibh euismod</p></div>
    <div class="legend" style="left:170px;top:134px;--c:var(--ink)"><h5>Lorem ipsum</h5><p class="fine">Lorem ipsum dolor sit amet, consectetuer adipiscing elit, sed diam nonummy nibh euismod</p></div>
    <div class="legend" style="left:250px;top:134px;--c:var(--gold)"><h5 class="gold">Lorem ipsum</h5><p class="fine">Lorem ipsum dolor sit amet, consectetuer adipiscing elit, sed diam nonummy nibh euismod</p></div>
    <div class="footer-rule"></div><div class="footer-brand"><i></i>TARVEL WORKS</div><div class="footer-mark"></div>
  </section>

  <!-- 8 About our project -->
  <section class="slide dark">
    <div class="photo" role="img" aria-label="Construction site with cranes in dark monochrome"></div>
    <div class="projframe">ABOUT<br>OUR<br><span>PROJECT</span></div>
  </section>

  <!-- 9 Portfolio -->
  <section class="slide">
    <h2 class="title" style="left:14px;top:9px">Portfolio of <b>projects</b></h2>
    <div class="fine abs" style="left:14px;top:28px;width:160px">
      <p>Lorem ipsum dolor sit amet, consectetuer adipiscing elit, sed diam nonummy nibh euismod tincidunt ut laoreet dolore magna aliquam erat volutpat. Ut wisi enim ad minim veniam, quis nostrud exerci tation ullamcorper suscipit lobortis nisl ut aliquip ex ea commodo consequat. Duis autem vel eum iriure dolor in hendrerit in vulputate velit esse</p>
      <p>Lorem ipsum dolor sit amet, consectetuer adipiscing elit, sed diam nonummy nibh euismod tincidunt ut laoreet dolore magna aliquam erat volutpat. Ut wisi enim ad minim veniam, quis nostrud exerci tation ullamcorper suscipit lobortis nisl ut aliquip ex ea commodo consequat. Duis autem vel eum iriure dolor in hendrerit in vulputate velit esse</p>
    </div>
    <div class="bullet" style="left:14px;top:118px;width:160px">Lorem ipsum dolor sit amet, consectetuer adipiscing elit, sed diam nonummy nibh euismod tincidunt ut laoreet dolore magna</div>
    <div class="bullet hollow" style="left:14px;top:140px;width:160px">Lorem ipsum dolor sit amet, consectetuer adipiscing elit, sed diam nonummy nibh euismod tincidunt ut laoreet dolore magna</div>
    <div class="abs" style="left:184px;top:26px;width:121px;height:120px;border:1px solid #9a9a9c;padding:3px">
      <div class="photo" style="inset:3px;background:linear-gradient(175deg,#dce6f0,#7e9bbd 45%,#33507a)" role="img" aria-label="Blue glass skyscrapers viewed from street level"></div>
    </div>
    <div class="footer-rule"></div><div class="footer-brand"><i></i>TARVEL WORKS</div><div class="footer-mark"></div>
  </section>

  <!-- 10 Use cases -->
  <section class="slide">
    <h2 class="title" style="left:17px;top:12px;font-size:20px;font-weight:400">Use <b>cases</b></h2>
    <div class="fine abs" style="left:16px;top:67px;width:133px">
      <p>Lorem ipsum dolor sit amet, consectetuer adipiscing elit, sed diam nonummy nibh euismod tincidunt ut laoreet dolore magna aliquam erat volutpat. Ut wisi enim ad minim veniam, quis nostrud exerci tation ullamcorper suscipit lobortis nisl ut aliquip ex ea commodo consequat. Duis autem vel eum iriure dolor in hendrerit i</p>
      <p>Lorem ipsum dolor sit amet, consectetuer adipiscing elit, sed diam nonummy nibh euismod tincidunt ut laoreet dolore magna aliquam erat volutpat. Ut wisi enim ad minim veniam, quis nostrud exerci tation ullamcorper suscipit lobortis nisl ut aliquip ex ea commodo consequat. Duis autem vel eum iriure dolor in hendrerit in</p>
    </div>
    <div class="phone" style="left:168px;top:21px;height:76px"><h6>Lorem<br>ipsum dolor</h6><div class="ico"></div><p class="fine">To introduce the students to the changing landscape of marketing and equip them with knowledge and tools</p></div>
    <div class="phone" style="left:216px;top:45px;height:79px"><h6>Dolor sit<br>amet, conse</h6><div class="ico"></div><p class="fine">You will learn concepts and ideas in digital marketing as well as how to use different tools and strategies</p></div>
    <div class="phone" style="left:264px;top:72px;height:79px"><h6>Consec</h6><div class="ico"></div><p class="fine">You are required to pass 80% of the evaluation test to obtain the certificate. The test can only be taken 3 times.</p></div>
    <div class="footer-rule"></div><div class="footer-brand"><i></i>TARVEL WORKS</div><div class="footer-mark"></div>
  </section>

  <!-- 11 Lorem ipsum project -->
  <section class="slide">
    <h2 class="title" style="left:13px;top:10px">Lorem ipsum <b>project</b></h2>
    <div class="fine abs" style="left:13px;top:31px;width:297px;font-size:4.6px;color:var(--ink-soft)">
      <p>Lorem ipsum dolor sit amet, consectetuer adipiscing elit, sed diam nonummy nibh euismod tincidunt ut laoreet dolore magna aliquam erat volutpat. Ut wisi enim ad minim veniam, quis nostrud exerci tation ullamcorper suscipit lobortis nisl utea commodo consequat. Duis autem vel eum iriure dolor in hendrerit i</p>
      <p>Lorem ipsum dolor sit amet, consectetuer adipiscing elit, sed diam nonummy nibh euismod tincidunt ut laoreet dolore magna aliquam erat volutpat.</p>
    </div>
    <div class="thumb" style="left:13px"><div class="photo" style="background:linear-gradient(135deg,#1e3a5c,#4a78a8 50%,#c9a06a)" role="img" aria-label="Hand touching a glowing digital screen"></div><h5>Lorem ipsum</h5><p class="fine">Lorem ipsum dolor sit amet, consectetuer adipiscing elit, sed diam nonummy nibh euismod tincidunt ut laoreet</p></div>
    <div class="thumb" style="left:89px"><div class="photo" style="background:linear-gradient(135deg,#e8eaec,#9fa8b2 55%,#3a3f48)" role="img" aria-label="Business team meeting in a bright office"></div><h5>Lorem ipsum</h5><p class="fine">Lorem ipsum dolor sit amet, consectetuer adipiscing elit, sed diam nonummy nibh euismod tincidunt ut laoreet</p></div>
    <div class="thumb" style="left:165px"><div class="photo" style="background:radial-gradient(circle at 50% 45%,#5aa8e8,#1c3f7a 60%,#0c1a38)" role="img" aria-label="Finger pressing a blue holographic interface"></div><h5>Lorem ipsum</h5><p class="fine">Lorem ipsum dolor sit amet, consectetuer adipiscing elit, sed diam nonummy nibh euismod tincidunt ut laoreet</p></div>
    <div class="thumb" style="left:241px"><div class="photo" style="background:linear-gradient(135deg,#10324a,#2f7a8e 55%,#7ab8c0)" role="img" aria-label="Agile workflow icons over a teal digital background"></div><h5>Lorem ipsum</h5><p class="fine">Lorem ipsum dolor sit amet, consectetuer adipiscing elit, sed diam nonummy nibh euismod tincidunt ut laoreet</p></div>
    <div class="footer-rule"></div><div class="footer-brand"><i></i>TARVEL WORKS</div><div class="footer-mark"></div>
  </section>

  <!-- 12 Price lists -->
  <section class="slide">
    <h2 class="title" style="left:9px;top:8px">Price <b>lists</b></h2>
    <div class="plan" style="left:55px;background:linear-gradient(180deg,#4a4a50,#a8a8ac 20%,#8f8f93)">
      <div class="stars">★</div><div class="tab">STANDART</div>
      <p class="head">Lorem ipsum dolor sit amet, consectetuer.</p>
      <ul><li>Lorem ipsum dolor</li><li>Lorem ipsum dolor</li><li>Lorem ipsum dolor</li><li>Lorem ipsum dolor</li><li>Lorem ipsum dolor</li><li>Lorem ipsum dolor</li></ul>
      <div class="buy">BUY NOW</div>
      <div class="price">14<sup>99</sup></div><p class="note">Lorem ipsum dolor sit amet, consectetuer adipiscing.</p>
    </div>
    <div class="plan" style="left:128px;background:linear-gradient(180deg,#1f1f23,#3a3a40 20%,#2d2d33)">
      <div class="stars">★★</div><div class="tab">BUSINESS</div>
      <p class="head">Lorem ipsum dolor sit amet, consectetuer.</p>
      <ul><li>Lorem ipsum dolor</li><li>Lorem ipsum dolor</li><li>Lorem ipsum dolor</li><li>Lorem ipsum dolor</li><li>Lorem ipsum dolor</li><li>Lorem ipsum dolor</li></ul>
      <div class="buy">BUY NOW</div>
      <div class="price">34<sup>99</sup></div><p class="note">Lorem ipsum dolor sit amet, consectetuer adipiscing.</p>
    </div>
    <div class="plan" style="left:201px;background:linear-gradient(180deg,#b8862c,#e4b65c 20%,#d3a444)">
      <div class="stars">★★★</div><div class="tab" style="background:var(--gold-dark)">PREMIUM</div>
      <p class="head">Lorem ipsum dolor sit amet, consectetuer.</p>
      <ul><li>Lorem ipsum dolor</li><li>Lorem ipsum dolor</li><li>Lorem ipsum dolor</li><li>Lorem ipsum dolor</li><li>Lorem ipsum dolor</li><li>Lorem ipsum dolor</li></ul>
      <div class="buy">BUY NOW</div>
      <div class="price" style="border-color:var(--gold)">54<sup>99</sup></div><p class="note">Lorem ipsum dolor sit amet, consectetuer adipiscing.</p>
    </div>
    <div class="footer-rule"></div><div class="footer-brand"><i></i>TARVEL WORKS</div><div class="footer-mark"></div>
  </section>

  <!-- 13 Two columns -->
  <section class="slide">
    <div class="abs" style="left:17px;top:9px;width:151px;height:150px;background:var(--panel)"></div>
    <h2 class="title" style="left:28px;top:16px;font-size:10px">Lorem ipsum<br><b>dolor sit amet</b></h2>
    <div class="fine abs" style="left:28px;top:42px;width:135px">
      <p>Lorem ipsum dolor sit amet, consectetuer adipiscing elit, sed diam nonummy nibh euismod tincidunt ut laoreet dolore magna aliquam erat volutpat. Ut wisi enim ad minim veniam, quis nostrud exerci tation ullamcorper suscipit lobortis nisl ut aliquip ex ea commodo consequat. Duis autem vel eum iriure dolor in hendrerit in vulputate velit esse</p>
      <p>Lorem ipsum dolor sit amet, consectetuer adipiscing elit, sed diam nonummy nibh euismod tincidunt ut laoreet dolore magna aliquam erat volutpat. Ut wisi enim ad minim veniam, quis nostrud exerci tation ullamcorper suscipit lobortis nisl ut aliquip ex ea commodo consequat. Duis autem vel eum iriure dolor in hendrerit in vulputate velit esse</p>
    </div>
    <div class="bullet" style="left:28px;top:118px;width:135px">Lorem ipsum dolor sit amet, consectetuer adipiscing elit, sed diam nonummy nibh euismod tincidunt ut laoreet dolore magna</div>
    <div class="bullet hollow" style="left:28px;top:138px;width:135px">Lorem ipsum dolor sit amet, consectetuer adipiscing elit, sed diam nonummy nibh euismod tincidunt ut laoreet dolore magna</div>
    <h2 class="title" style="left:176px;top:16px;font-size:10px;font-weight:700"><b style="font-weight:500">Lorem ipsum</b><br>dolor sit amet</h2>
    <div class="fine abs" style="left:176px;top:42px;width:135px">
      <p>Lorem ipsum dolor sit amet, consectetuer adipiscing elit, sed diam nonummy nibh euismod tincidunt ut laoreet dolore magna aliquam erat volutpat. Ut wisi enim ad minim veniam, quis nostrud exerci tation ullamcorper suscipit lobortis nisl ut aliquip ex ea commodo consequat. Duis autem vel eum iriure dolor in hendrerit in vulputate velit esse</p>
      <p>Lorem ipsum dolor sit amet, consectetuer adipiscing elit, sed diam nonummy nibh euismod tincidunt ut laoreet dolore magna aliquam erat volutpat. Ut wisi enim ad minim veniam, quis nostrud exerci tation ullamcorper suscipit lobortis nisl ut aliquip ex ea commodo consequat. Duis autem vel eum iriure dolor in hendrerit in vulputate velit esse</p>
    </div>
    <div class="bullet" style="left:176px;top:118px;width:135px;--x:0">Lorem ipsum dolor sit amet, consectetuer adipiscing elit, sed diam nonummy nibh euismod tincidunt ut laoreet dolore magna</div>
    <div class="bullet hollow" style="left:176px;top:138px;width:135px">Lorem ipsum dolor sit amet, consectetuer adipiscing elit, sed diam nonummy nibh euismod tincidunt ut laoreet dolore magna</div>
    <div class="footer-rule"></div><div class="footer-brand"><i></i>TARVEL WORKS</div><div class="footer-mark"></div>
  </section>

  <!-- 14 Kites -->
  <section class="slide">
    <h2 class="title" style="left:10px;top:10px">Lorem ipsum <b>dolor sit amet</b></h2>
    <svg class="abs" style="left:0;top:0" width="323" height="181" viewBox="0 0 323 181" font-family="Montserrat,sans-serif">
      <polyline fill="none" stroke="#bdbdc0" stroke-width=".5" points="66,44 113,52 161,29 209,26 255,35"/>
      <g stroke="#9a9a9c" stroke-width=".5" stroke-dasharray="1 1"><path d="M66 44v8M113 52v6M161 29v10M209 26v10M255 35v10"/></g>
      <g fill="#fff" stroke-width=".8"><circle cx="66" cy="44" r="1.8" stroke="#d3a444"/><circle cx="113" cy="52" r="1.8" stroke="#2d2d33"/><circle cx="161" cy="29" r="1.8" stroke="#d3a444"/><circle cx="209" cy="26" r="1.8" stroke="#2d2d33"/><circle cx="255" cy="35" r="1.8" stroke="#d3a444"/></g>
      <g>
        <path d="M66 52l20 42-20 14-20-14z" fill="#2d2d33"/><path d="M66 52l20 42-20 14z" fill="#4a4a52"/>
        <path d="M113 58l20 30-20 18-20-18z" fill="#d3a444"/><path d="M113 58l20 30-20 18z" fill="#b8862c"/>
        <path d="M161 39l20 50-20 17-20-17z" fill="#2d2d33"/><path d="M161 39l20 50-20 17z" fill="#4a4a52"/>
        <path d="M209 36l20 52-20 18-20-18z" fill="#d3a444"/><path d="M209 36l20 52-20 18z" fill="#b8862c"/>
        <path d="M255 45l20 45-20 16-20-16z" fill="#2d2d33"/><path d="M255 45l20 45-20 16z" fill="#4a4a52"/>
      </g>
      <g fill="#fff"><circle cx="53" cy="94" r="4"/><circle cx="100" cy="90" r="4"/><circle cx="148" cy="91" r="4"/><circle cx="196" cy="90" r="4"/><circle cx="242" cy="92" r="4"/></g>
      <g fill="#fff" font-size="4" font-weight="700" text-anchor="middle">
        <text transform="translate(72 88) rotate(-90)">Title One</text>
        <text transform="translate(119 86) rotate(-90)">Title Two</text>
        <text transform="translate(167 86) rotate(-90)">Title Three</text>
        <text transform="translate(215 86) rotate(-90)">Title Four</text>
      </g>
      <g fill="none" stroke="#2d2d33" stroke-width=".8"><path d="M58 121l8 5 8-5M105 121l8 5 8-5M153 121l8 5 8-5M201 121l8 5 8-5M247 121l8 5 8-5"/></g>
    </svg>
    <span class="kite-val" style="left:59px;top:36px">$1000</span>
    <span class="kite-val" style="left:107px;top:44px">$750</span>
    <span class="kite-val" style="left:155px;top:21px">$1200</span>
    <span class="kite-val" style="left:203px;top:18px">$1400</span>
    <span class="kite-val" style="left:249px;top:27px">$1100</span>
    <span class="kite-year" style="left:51px">2014</span><span class="kite-year" style="left:98px">2016</span><span class="kite-year" style="left:146px">2018</span><span class="kite-year" style="left:194px">2020</span><span class="kite-year" style="left:240px">2022</span>
    <p class="kite-text" style="left:44px">Lorem ipsum dolor sit amet, consectetuer adipiscing elit, sed diam nonummy nibh euismod tincid</p>
    <p class="kite-text" style="left:92px">Lorem ipsum dolor sit amet, consectetuer adipiscing elit, sed diam nonummy nibh euismod tincid</p>
    <p class="kite-text" style="left:140px">Lorem ipsum dolor sit amet, consectetuer adipiscing elit, sed diam nonummy nibh euismod tincid</p>
    <p class="kite-text" style="left:188px">Lorem ipsum dolor sit amet, consectetuer adipiscing elit, sed diam nonummy nibh euismod tincid</p>
    <p class="kite-text" style="left:236px">Lorem ipsum dolor sit amet, consectetuer adipiscing elit, sed diam nonummy nibh euismod tincid</p>
    <div class="footer-rule"></div><div class="footer-brand"><i></i>TARVEL WORKS</div><div class="footer-mark"></div>
  </section>

  <!-- 15 Benefits -->
  <section class="slide">
    <h2 class="title" style="left:12px;top:12px">Benefits to <b>each customer</b></h2>
    <div class="fine abs" style="left:13px;top:40px;width:157px">
      <p>Lorem ipsum dolor sit amet, consectetuer adipiscing elit, sed diam nonummy nibh euismod tincidunt ut laoreet dolore magna aliquam erat volutpat. Ut wisi enim ad minim veniam, quis nostrud exerci tation ullam</p>
      <p>Lorem ipsum dolor sit amet, consectetuer adipiscing elit, sed diam nonummy nibh euismod tincidunt ut laoreet dolore magna aliquam erat volutpat. Ut wisi enim ad minim veniam, quis nostrud exerci tation ullam</p>
      <p>Lorem ipsum dolor sit amet, consectetuer adipiscing elit, sed diam nonummy nibh euismod tincidunt ut laoreet dolore magna aliquam erat volutpat. Ut wisi enim ad minim veniam, quis nostrud exerci</p>
      <p>Lorem ipsum dolor sit amet, consectetuer adipiscing elit, sed diam nonummy nibh euismod tincidunt ut laoreet dolore magna aliquam erat volutpat. Ut wisi enim ad minim veniam, quis nostrud exerci tation ullam<br>Lorem ipsum dolor sit amet, consectetuer adipiscing elit, sed diam nonummy nibh euismod tincidunt ut laoreet dolore magna</p>
    </div>
    <div class="photo" style="left:183px;top:39px;width:122px;height:113px;background:linear-gradient(135deg,#f2f2f2,#bdbdbf 45%,#6c6c70)" role="img" aria-label="Smiling colleagues working together at a computer, black and white"></div>
    <div class="footer-rule"></div><div class="footer-brand"><i></i>TARVEL WORKS</div><div class="footer-mark"></div>
  </section>

  <!-- 16 Timeline -->
  <section class="slide">
    <h2 class="title" style="left:8px;top:10px">Timeline of <b>roadmap</b></h2>
    <svg class="abs" style="left:0;top:0" width="323" height="181" viewBox="0 0 323 181" font-family="Montserrat,sans-serif" font-weight="700" text-anchor="middle">
      <path d="M275 158c-40 0-75-2-100-8s-40-20-28-28c12-8 40-6 60-8 18-2 10-18 0-24" fill="none" stroke="#d3a444" stroke-width="1.2"/>
      <path d="M207 90c-15-6-30-6-38-2" fill="none" stroke="#d3a444" stroke-width="1.2"/>
      <path d="M169 88c-10-8-4-18 4-22s16-12 10-18c-8-6-20 0-34-4" fill="none" stroke="#d3a444" stroke-width="1.2"/>
      <path d="M149 44c-10-4-14-10-12-14" fill="none" stroke="#d3a444" stroke-width="1.2"/>
      <g stroke="#2d2d33" stroke-width="1" stroke-dasharray="1 1.5"><path d="M275 130v28M166 110v40"/></g>
      <circle cx="275" cy="158" r="1.6" fill="#2d2d33"/><circle cx="166" cy="122" r="1.6" fill="#2d2d33"/>
      <circle cx="273" cy="110" r="20" fill="#fff" stroke="#2d2d33" stroke-width="4"/><text x="273" y="122" font-size="30" fill="#d3a444" font-weight="500">1</text>
      <circle cx="229" cy="69" r="9" fill="#fff" stroke="#2d2d33" stroke-width="2"/><text x="229" y="74" font-size="13" fill="#d3a444" font-weight="500">3</text>
      <circle cx="183" cy="90" r="11" fill="#fff" stroke="#2d2d33" stroke-width="2.4"/><text x="183" y="96" font-size="16" fill="#d3a444" font-weight="500">2</text>
      <circle cx="149" cy="66" r="6.5" fill="#fff" stroke="#2d2d33" stroke-width="1.6"/><text x="149" y="69.5" font-size="9" fill="#d3a444" font-weight="500">4</text>
      <circle cx="170" cy="53" r="5" fill="#fff" stroke="#2d2d33" stroke-width="1.3"/><text x="170" y="56" font-size="7" fill="#d3a444" font-weight="500">5</text>
      <circle cx="131" cy="49" r="3.6" fill="#fff" stroke="#2d2d33" stroke-width="1"/><text x="131" y="51.3" font-size="5" fill="#d3a444" font-weight="500">6</text>
    </svg>
    <div class="tl-label" style="left:82px;top:48px"><h6>Lorem Ipsum</h6><p class="fine">Lorem ipsum dolor sit amet, consectetuer adipiscing elit, sed diam nonummy nibh euismod tincid</p></div>
    <div class="tl-label" style="left:158px;top:42px"><h6>Lorem Ipsum</h6><p class="fine">Lorem ipsum dolor sit amet, consectetuer adipiscing elit, sed diam nonummy nibh euismod tincid</p></div>
    <div class="tl-label" style="left:228px;top:44px"><h6>Lorem Ipsum</h6><p class="fine">Lorem ipsum dolor sit amet, consectetuer adipiscing elit, sed diam nonummy nibh euismod tincid</p></div>
    <div class="tl-label" style="left:116px;top:89px"><h6>Lorem Ipsum</h6><p class="fine">Lorem ipsum dolor sit amet, consectetuer adipiscing elit, sed diam nonummy nibh euismod tincid</p></div>
    <div class="tl-label" style="left:217px;top:113px"><h6>Lorem Ipsum</h6><p class="fine">Lorem ipsum dolor sit amet, consectetuer adipiscing elit, sed diam nonummy nibh euismod tincid</p></div>
    <div class="abs" style="left:15px;top:105px;font-size:8px;font-weight:500">FOR 2 YEARS</div>
    <div class="yearbadge" style="left:15px"><div class="dot">A</div><div><h6>2019</h6><p class="fine">Lorem ipsum dolor sit amet, consectetuer adipiscing elit, sed diam</p></div></div>
    <div class="yearbadge" style="left:88px"><div class="dot">B</div><div><h6>2020</h6><p class="fine">Lorem ipsum dolor sit amet, consectetuer adipiscing elit, sed diam</p></div></div>
    <div class="footer-rule"></div><div class="footer-brand"><i></i>TARVEL WORKS</div><div class="footer-mark"></div>
  </section>

  <!-- 17 Organizational chart -->
  <section class="slide">
    <h2 class="title" style="left:15px;top:11px;font-weight:700;color:var(--ink-soft)">Organizational <b>chart</b></h2>
    <div class="fine abs" style="left:15px;top:28px;width:292px;font-size:4.6px;color:var(--ink-soft)">
      <p>Lorem ipsum dolor sit amet, consectetuer adipiscing elit, sed diam nonummy nibh euismod tincidunt ut laoreet dolore magna aliquam erat volutpat. Ut wisi enim ad minim veniam, quis nostrud exerci tation ullamcorper suscipit lobortis nisl ut aliquip ex ea commodo consequat. Duis autem</p>
      <p>Lorem ipsum dolor sit amet, cons ectetuer adipiscing elit, sed diam nonummy nibh euismod tincidunt ut laoreet dolore magna aliquam erat volutpat.</p>
    </div>
    <div class="band"></div>
    <div class="person" style="left:14px"><div class="avatar" role="img" aria-label="Portrait photo of team member"></div><h5>JONAH REED</h5><p class="fine">Ipsum dolor sit amet, cons ectetuer adipiscing elit, sed diam nonummy nibh euismod tincidunt ut laoreet dolore magna aliquam erat volutpat</p></div>
    <div class="person" style="left:92px"><div class="avatar" role="img" aria-label="Portrait photo of team member"></div><h5>MIRA HALE</h5><p class="fine">Ipsum dolor sit amet, cons ectetuer adipiscing elit, sed diam nonummy nibh euismod tincidunt ut laoreet dolore magna aliquam erat volutpat</p></div>
    <div class="person" style="left:168px"><div class="avatar" role="img" aria-label="Portrait photo of team member"></div><h5>JONAH REED</h5><p class="fine">Ipsum dolor sit amet, cons ectetuer adipiscing elit, sed diam nonummy nibh euismod tincidunt ut laoreet dolore magna aliquam erat volutpat</p></div>
    <div class="person" style="left:246px"><div class="avatar" role="img" aria-label="Portrait photo of team member"></div><h5>MIRA HALE</h5><p class="fine">Ipsum dolor sit amet, cons ectetuer adipiscing elit, sed diam nonummy nibh euismod tincidunt ut laoreet dolore magna aliquam erat volutpat</p></div>
    <div class="footer-rule"></div><div class="footer-brand"><i></i>TARVEL WORKS</div><div class="footer-mark"></div>
  </section>

  <!-- 18 Contact -->
  <section class="slide contact">
    <div class="photo" role="img" aria-label="Tower under construction with cranes rising out of fog"></div>
    <div class="social"><i></i><i></i><i></i><i></i></div>
    <div class="brand"><i></i>TARVEL WORKS</div>
    <h3>Contact <b>US</b></h3>
    <ul class="clist">
      <li><i></i>555-010-2030</li>
      <li><i></i>info@tarvelworks.com</li>
      <li><i></i>12 Harbour Lane, Westfield, box 4410</li>
    </ul>
    <div class="url">www.tarvelworks.com</div>
  </section>

</main>
</body>
</html>
```